Square Business Cards for Our Restaurant / Event Venue

We need square business cards designed for the management team of our event venue and restaurant. On one side of the card should be the the Harbor Lantern 7 logo and URL www.harborlantern7.example. On the other side should be the Ember Logo and URL www.emberhall7.example. All employee details should be on the side with Ember logo. There will be a total of 5 cards to be created with the design.

Clara Bennquist
clara@harborlantern7.example

main 555.418.3072
direct 555.730.2946

4831 West Orchard Lane SE
Washington, DC 90417

Industry/Entity Type

Business

```html
<!DOCTYPE html>
<html lang="en">
<head>
<meta charset="utf-8">
<title>Ember / Harbor Lantern 7 Business Cards</title>
<link rel="stylesheet" href="https://fonts.googleapis.com/css2?family=Roboto:wght@400;700&family=Roboto+Condensed:wght@700&display=swap">
<style>
  :root {
    --brand-red: #b71c1f;
    --ink: #111111;
    --text-grey: #555555;
    --card-white: #f4f4f4;
    --page-bg: #e8e5e1;
    --divider: #c9c9c9;
  }
  * { margin: 0; padding: 0; box-sizing: border-box; }
  html, body {
    width: 1200px;
    height: 960px;
    overflow: hidden;
    background: var(--page-bg);
    font-family: "Roboto", Arial, sans-serif;
  }
  .canvas { position: relative; width: 1200px; height: 960px; }
  .card {
    position: absolute;
    width: 600px;
    height: 342px;
    background: var(--card-white);
    box-shadow: 0 2px 6px rgba(0,0,0,0.18);
    overflow: hidden;
  }
  .card--front { left: 302px; top: 130px; }
  .card--back { left: 299px; top: 489px; }

  .front-band { position: absolute; left: 0; top: 0; }
  .holder {
    position: absolute;
    right: 36px;
    top: 28px;
    text-align: right;
    color: #fff;
    font-family: "Roboto Condensed", "Arial Narrow", sans-serif;
    font-weight: 700;
  }
  .holder__name { font-size: 22px; letter-spacing: 0.2px; line-height: 26px; }
  .holder__title { font-size: 15px; line-height: 20px; }

  .venue-name {
    position: absolute;
    left: 50px;
    top: 178px;
    width: 210px;
    text-align: center;
    font-size: 50px;
    font-weight: 700;
    color: var(--ink);
    line-height: 60px;
  }
  .divider {
    position: absolute;
    left: 282px;
    top: 155px;
    width: 1px;
    height: 142px;
    background: var(--divider);
  }
  .contact {
    position: absolute;
    left: 309px;
    top: 160px;
    color: var(--text-grey);
    font-size: 14px;
    line-height: 19px;
  }
  .contact__address { margin-bottom: 9px; }
  .contact__list { list-style: none; }
  .contact__list li { display: flex; align-items: center; gap: 8px; }
  .contact__icon { width: 13px; height: 13px; flex: none; }

  .brand-mark {
    position: absolute;
    left: 204px;
    top: 61px;
    width: 190px;
    height: 190px;
    border-radius: 50%;
    background: var(--brand-red);
    display: flex;
    align-items: center;
    justify-content: center;
    text-align: center;
    color: #fff;
    font-size: 27px;
    font-weight: 400;
    line-height: 32px;
  }
  .back-url {
    position: absolute;
    left: 0;
    right: 0;
    top: 290px;
    text-align: center;
    font-size: 14px;
    letter-spacing: 2.2px;
    color: var(--text-grey);
  }
  .back-url__domain { color: var(--brand-red); }
</style>
</head>
<body>
<main class="canvas">

  <section class="card card--front" aria-label="Ember card side">
    <svg class="front-band" width="600" height="342" viewBox="0 0 600 342" aria-hidden="true">
      <path d="M0,0 H600 V152 C480,92 310,22 160,42 C90,51 30,66 0,76 Z" fill="var(--brand-red)"/>
      <path d="M0,76 C30,66 90,51 160,42 C310,22 480,92 600,152 L600,156 C480,100 310,32 160,50 C90,58 30,74 0,86 Z" fill="var(--ink)"/>
    </svg>

    <div class="holder">
      <div class="holder__name">CLARA BENNQUIST</div>
      <div class="holder__title">CEO/FOUNDER</div>
    </div>

    <div class="venue-name">Ember</div>
    <div class="divider"></div>

    <div class="contact">
      <p class="contact__address">4831 West Orchard Lane SE<br>Washington, DC 90417</p>
      <ul class="contact__list">
        <li>
          <svg class="contact__icon" viewBox="0 0 16 16" aria-hidden="true"><path d="M3.5 1.5 L6 1 L7.3 4.6 L5.6 6 C6.5 7.9 8.1 9.5 10 10.4 L11.4 8.7 L15 10 L14.5 12.5 C14.2 14 12.8 15 11.3 14.8 C6.2 14 2 9.8 1.2 4.7 C1 3.2 2 1.8 3.5 1.5 Z" fill="var(--brand-red)"/></svg>
          <span>555.418.3072</span>
        </li>
        <li>
          <svg class="contact__icon" viewBox="0 0 16 16" aria-hidden="true"><path d="M3.5 1.5 L6 1 L7.3 4.6 L5.6 6 C6.5 7.9 8.1 9.5 10 10.4 L11.4 8.7 L15 10 L14.5 12.5 C14.2 14 12.8 15 11.3 14.8 C6.2 14 2 9.8 1.2 4.7 C1 3.2 2 1.8 3.5 1.5 Z" fill="var(--brand-red)"/></svg>
          <span>555.730.2946</span>
        </li>
        <li>
          <svg class="contact__icon" viewBox="0 0 16 16" aria-hidden="true"><rect x="1" y="3.5" width="14" height="9.5" fill="var(--brand-red)"/><path d="M1.5 4 L8 9 L14.5 4" fill="none" stroke="#fff" stroke-width="1.3"/></svg>
          <span>clara@harborlantern7.example</span>
        </li>
        <li>
          <svg class="contact__icon" viewBox="0 0 16 16" aria-hidden="true"><circle cx="8" cy="8" r="6.5" fill="var(--brand-red)"/><path d="M1.5 8 H14.5 M8 1.5 C5 5 5 11 8 14.5 M8 1.5 C11 5 11 11 8 14.5" fill="none" stroke="#fff" stroke-width="1"/></svg>
          <span>www.emberhall7.example</span>
        </li>
      </ul>
    </div>
  </section>

  <section class="card card--back" aria-label="Harbor Lantern 7 card side">
    <div class="brand-mark">Harbor<br>Lantern 7</div>
    <p class="back-url">www.<span class="back-url__domain">harborlantern7</span>.example</p>
  </section>

</main>
</body>
</html>
```